Brivond Technologies business card design

We need a business card designed with our new logo. it would be great if the card could communicate it is a technology based company.

Target Market(s)

system integrators

Industry/Entity Type

technology, IOT

Contact Information for Business Card

Name, designation, Address, telephone number, email address

Requirements
Must have
• logo and company name
Nice to have
• something to do with technology

```html
<!DOCTYPE html>
<html lang="en">
<head>
<meta charset="utf-8">
<title>Brivond Technologies – Business Card</title>
<link href="https://fonts.googleapis.com/css2?family=Montserrat:wght@500;600;700&display=swap" rel="stylesheet">
<style>
  :root {
    --page: #e4e4e6;
    --charcoal: #3d3d41;
    --orange: #f39019;
    --ink: #2b2b2e;
    --white: #ffffff;
    --silver: #d9d9dc;
  }
  * { margin: 0; padding: 0; box-sizing: border-box; }
  html, body { width: 1200px; height: 886px; overflow: hidden; }
  body {
    background: var(--page);
    font-family: "Montserrat", sans-serif;
    position: relative;
  }
  .card {
    position: absolute;
    left: 250px;
    width: 700px;
    height: 400px;
    border-radius: 4px;
    overflow: hidden;
    box-shadow: 0 6px 18px rgba(0,0,0,.18);
  }
  /* Back side */
  .card-back { top: 28px; background: var(--charcoal); }
  .world-map-area {
    position: absolute;
    left: 70px; top: 50px;
    width: 560px; height: 300px;
    border-radius: 40px;
    background: radial-gradient(ellipse at center, rgba(255,255,255,.10) 0%, rgba(255,255,255,.05) 55%, rgba(255,255,255,0) 75%);
  }
  .back-brand {
    position: absolute;
    left: 0; right: 0; top: 172px;
    display: flex; align-items: center; justify-content: center; gap: 14px;
  }
  .back-brand .brand-square { width: 22px; height: 22px; background: var(--silver); }
  .back-brand .brand-name {
    color: var(--silver);
    font-weight: 700;
    font-size: 38px;
    letter-spacing: 1px;
    text-transform: uppercase;
  }
  /* Front side */
  .card-front { top: 458px; background: var(--white); }
  .front-wave { position: absolute; inset: 0; }
  .front-brand {
    position: absolute;
    left: 36px; top: 150px;
    display: flex; align-items: center; gap: 9px;
  }
  .front-brand .brand-square { width: 14px; height: 14px; background: var(--orange); }
  .front-brand .brand-name {
    color: var(--charcoal);
    font-weight: 700;
    font-size: 18px;
    letter-spacing: .3px;
    text-transform: uppercase;
    white-space: nowrap;
  }
  .divider {
    position: absolute;
    left: 352px; top: 40px;
    width: 2px; height: 196px;
    background: var(--orange);
  }
  .contact {
    position: absolute;
    left: 376px; top: 36px;
    color: var(--ink);
    font-weight: 500;
    font-size: 14px;
    line-height: 1.35;
  }
  .contact-name {
    color: var(--orange);
    font-weight: 700;
    font-size: 20px;
    text-transform: uppercase;
    line-height: 1.15;
  }
  .contact-title { margin-bottom: 10px; }
  .contact-address { margin-bottom: 10px; }
  .contact-line { display: flex; align-items: center; gap: 10px; margin-bottom: 2px; }
  .contact-line svg { width: 14px; height: 14px; flex: none; }
</style>
</head>
<body>

  <section class="card card-back">
    <div class="world-map-area" role="img" aria-label="Dotted world map in soft grey behind the company name"></div>
    <div class="back-brand">
      <span class="brand-square"></span>
      <span class="brand-name">Brivond Technologies</span>
    </div>
  </section>

  <section class="card card-front">
    <svg class="front-wave" viewBox="0 0 700 400" preserveAspectRatio="none" aria-hidden="true">
      <path d="M0,312 C130,328 240,338 340,312 C450,284 560,238 700,230 L700,400 L0,400 Z" fill="var(--charcoal)"/>
      <path d="M130,324 C240,330 340,306 432,270 C530,234 610,222 690,218 C610,228 532,244 436,280 C340,316 240,334 130,324 Z" fill="var(--orange)" stroke="var(--orange)" stroke-width="2.5"/>
    </svg>

    <div class="front-brand">
      <span class="brand-square"></span>
      <span class="brand-name">Brivond Technologies</span>
    </div>

    <div class="divider"></div>

    <div class="contact">
      <p class="contact-name">Dalen Whitcombe</p>
      <p class="contact-title">Owner/Co-Founder</p>
      <p class="contact-address">Corvane Plaza 2710 Elm<br>Halvester RD Suite 118</p>
      <p class="contact-line">
        <svg viewBox="0 0 16 16"><path d="M3 1.5l3 3-1.6 1.6a8 8 0 0 0 5.5 5.5L11.5 10l3 3-2 2C6.5 15 1 9.5 1 3.5z" fill="var(--orange)"/></svg>
        555-013-4472
      </p>
      <p class="contact-line">
        <svg viewBox="0 0 16 16"><rect x="1" y="3" width="14" height="10" fill="var(--orange)"/><path d="M1 3l7 6 7-6" fill="none" stroke="var(--white)" stroke-width="1.3"/></svg>
        info@brivondtech.com
      </p>
      <p class="contact-line">
        <svg viewBox="0 0 16 16"><circle cx="8" cy="8" r="7" fill="var(--orange)"/><path d="M1 8h14M8 1c-3 3-3 11 0 14M8 1c3 3 3 11 0 14" fill="none" stroke="var(--white)" stroke-width="1"/></svg>
        www.brivondtech.com
      </p>
    </div>
  </section>

</body>
</html>
```